Looking for a new business card design

We are looking for a corporate looking yet still a bit different then the rest. I would like the card black with the picture on the back and the phrase "Guiding every crew to zero harm" on the back as well. Then a clean look on the front with a bit of an edge.

Target Market(s)

Corporate oil executives and drilling supervisors

Industry/Entity Type

Oil And Gas

Contact Information for Business Card

Black, bold, clean lines.

Font styles to use
Sans Serif

Requirements
Must have
• Picture on the back with the slogan "Guiding every crew to zero harm"
• Black background
• Stands out

```html
<!DOCTYPE html>
<html lang="en">
<head>
<meta charset="utf-8">
<title>Corvane Energy Services Corp. – Business Card</title>
<link rel="stylesheet" href="https://fonts.googleapis.com/css2?family=Arimo:wght@400;700&display=swap">
<style>
  :root {
    --backdrop: #c5d0ce;
    --card-black: #050606;
    --royal-blue: #0033b3;
    --mid-blue: #2360ad;
    --sky-blue: #6bb8f5;
    --lime: #c6dc14;
    --white: #ffffff;
    --steel-grey: #6b7073;
    --divider: #8a8f93;
    --photo-dark: #0d1420;
    --photo-mid: #2f3d55;
    --photo-light: #7d8ca3;
  }
  * { margin: 0; padding: 0; box-sizing: border-box; }
  html, body {
    width: 1200px; height: 575px; overflow: hidden;
    background: var(--backdrop);
    font-family: "Arimo", Arial, sans-serif;
  }
  .canvas { position: relative; width: 1200px; height: 575px; }
  .card {
    position: absolute; top: 117px; height: 283px;
    background: var(--card-black); overflow: hidden;
  }
  .card svg.card-shapes { position: absolute; inset: 0; }
  .card-back { left: 74px; width: 494px; }
  .card-front { left: 632px; width: 499px; }

  .brand { position: absolute; display: flex; align-items: center; gap: 8px; }
  .brand-dot { width: 18px; height: 18px; border-radius: 50%; background: var(--mid-blue); flex: none; }
  .brand-name { color: var(--lime); font-weight: 700; letter-spacing: 0.3px; line-height: 1; white-space: nowrap; }
  .card-back .brand { left: 212px; top: 80px; }
  .card-back .brand-name { font-size: 27px; }
  .brand-tagline {
    position: absolute; left: 238px; top: 110px;
    color: var(--steel-grey); font-size: 10px; white-space: nowrap;
  }
  .slogan {
    position: absolute; left: 0; right: 0; top: 209px;
    text-align: center; color: var(--lime); font-size: 16px; line-height: 18px;
  }

  .holder-name {
    position: absolute; left: 30px; top: 24px;
    color: var(--white); font-size: 19px; line-height: 22px; white-space: nowrap;
  }
  .holder-position {
    position: absolute; left: 78px; top: 49px;
    color: var(--white); font-size: 14px; line-height: 16px;
  }
  .card-front .brand { left: 324px; top: 38px; }
  .card-front .brand-name { font-size: 26px; }

  .contact-item {
    position: absolute; top: 133px; width: 140px; margin-left: -70px;
    display: flex; flex-direction: column; align-items: center; gap: 18px;
    color: var(--white); font-size: 16px; line-height: 18px;
  }
  .contact-item svg { width: 28px; height: 28px; }
  .contact-email { left: 67px; }
  .contact-address { left: 246px; }
  .contact-phone { left: 418px; }
  .contact-divider {
    position: absolute; top: 145px; width: 1px; height: 93px;
    background: var(--divider);
  }
</style>
</head>
<body>
<main class="canvas">

  <section class="card card-back">
    <svg class="card-shapes" width="494" height="283" viewBox="0 0 494 283">
      <rect x="0" y="190" width="494" height="93" fill="var(--royal-blue)"/>
      <path d="M0 199 Q247 300 494 199 L494 240 Q247 250 0 240 Z" fill="var(--mid-blue)"/>
      <path d="M0 0 H494 V199 Q480 258 247 255 Q14 258 0 199 Z" fill="var(--card-black)"/>
      <rect x="134" y="0" width="227" height="30" fill="var(--sky-blue)"/>
      <rect x="163" y="0" width="168" height="30" fill="var(--mid-blue)"/>
    </svg>
    <div class="brand">
      <span class="brand-dot"></span>
      <span class="brand-name">CORVANE</span>
    </div>
    <p class="brand-tagline">Energy Services Corp.</p>
    <p class="slogan">Guiding every crew to zero harm</p>
  </section>

  <section class="card card-front">
    <svg class="card-shapes" width="499" height="283" viewBox="0 0 499 283">
      <defs>
        <radialGradient id="site-photo-tone" cx="0.5" cy="0.45" r="0.65">
          <stop offset="0" stop-color="var(--photo-light)"/>
          <stop offset="0.45" stop-color="var(--photo-mid)"/>
          <stop offset="1" stop-color="var(--photo-dark)"/>
        </radialGradient>
      </defs>
      <path d="M0 67 Q20 95 80 108 L0 106 Z" fill="var(--mid-blue)"/>
      <path d="M499 67 Q479 95 419 108 L499 106 Z" fill="var(--mid-blue)"/>
      <path role="img" aria-label="Aerial night photograph of an illuminated drilling site"
            d="M0 0 H499 V80 Q470 108 420 114 Q250 130 80 114 Q25 108 0 80 Z"
            fill="url(#site-photo-tone)"/>
      <rect x="135" y="253" width="227" height="30" fill="var(--mid-blue)"/>
      <rect x="164" y="253" width="169" height="30" fill="var(--royal-blue)"/>
    </svg>

    <p class="holder-name">Individual Name</p>
    <p class="holder-position">position</p>
    <div class="brand">
      <span class="brand-dot"></span>
      <span class="brand-name">CORVANE</span>
    </div>

    <div class="contact-item contact-email">
      <svg viewBox="0 0 28 28" aria-hidden="true">
        <rect x="2" y="8" width="24" height="17" fill="none" stroke="var(--white)" stroke-width="1.8"/>
        <path d="M2 8 L14 18 L26 8" fill="none" stroke="var(--white)" stroke-width="1.8"/>
        <circle cx="14" cy="7" r="4" fill="var(--white)"/>
        <circle cx="14" cy="7" r="1.6" fill="var(--card-black)"/>
      </svg>
      <span>E-mail</span>
    </div>
    <span class="contact-divider" style="left:167px"></span>
    <div class="contact-item contact-address">
      <svg viewBox="0 0 28 28" aria-hidden="true">
        <path d="M18 2 a6 6 0 0 1 6 6 c0 5 -6 11 -6 11 s-6 -6 -6 -11 a6 6 0 0 1 6 -6 Z" fill="var(--white)"/>
        <circle cx="18" cy="8" r="2.3" fill="var(--card-black)"/>
        <path d="M3 20 H12 L10 26 H1 Z M14 20 H22 L26 26 H12 Z" fill="var(--white)"/>
      </svg>
      <span>Address</span>
    </div>
    <span class="contact-divider" style="left:334px"></span>
    <div class="contact-item contact-phone">
      <svg viewBox="0 0 28 28" aria-hidden="true">
        <path d="M7 3 L11 3 L13 9 L10 11 Q12 16 17 18 L19 15 L25 17 L25 21 Q24 25 20 25 Q5 22 3 7 Q3 3 7 3 Z" fill="var(--white)"/>
      </svg>
      <span>Phone</span>
    </div>
  </section>

</main>
</body>
</html>
```